Business Card Design for Kind Helper

I am starting my own consultancy business, using what I learned in marketing and advertising to help Non -profits with marketing and communications needs. I need a professional business card design to hand out to my clients.

My business name is “Outreach2Kindness” my vision is that this need this to be reflective of marketing doing good for the world through the power of communications. I like the color palettes in olives, creams and oranges but am open to design options.
In addition to the cards I am asking for separate file for the logo and will need a JPG, PSD Vector File.

Information to go on the card:

Morwenna Calloway
Marketing Consultant
Email: outreach2kindness@mailbrook.com, callowaym1@brinmoreu.edu
Website: Outreach2Kindness.com

Communications

```html
<!DOCTYPE html>
<html lang="en">
<head>
<meta charset="utf-8">
<title>Outreach2Kindness – Business Card Options</title>
<link rel="stylesheet" href="https://fonts.googleapis.com/css2?family=Arimo:wght@400;700&display=swap">
<style>
  :root {
    --page: #ffffff;
    --card-grey: #f2f2f4;
    --card-white: #ffffff;
    --card-border: #ececec;
    --ink: #4a4a4a;
    --ink-dark: #1e1e1e;
    --sky: #29a8e0;
    --leaf: #8cc63f;
    --white: #ffffff;
  }
  * { box-sizing: border-box; margin: 0; padding: 0; }
  html, body {
    width: 1200px; height: 710px; overflow: hidden;
    background: var(--page);
    font-family: "Arimo", Arial, sans-serif;
  }
  .sheet { position: relative; width: 1200px; height: 710px; }

  .card {
    position: absolute;
    width: 519px; height: 279px;
    overflow: hidden;
  }
  .card--front { left: 59px; }
  .card--back  { left: 622px; background: var(--card-grey); }
  .row-top    { top: 58px; }
  .row-bottom { top: 376px; }

  .card--front.row-top    { background: var(--card-grey); }
  .card--front.row-bottom { background: var(--card-white); border: 2px solid var(--card-border); }

  /* Front: brand mark */
  .brand-dot {
    position: absolute; left: 50%; top: 52px;
    width: 110px; height: 110px; margin-left: -55px;
    border-radius: 50%;
  }
  .brand-dot--sky  { background: var(--sky); }
  .brand-dot--leaf { background: var(--leaf); }
  .brand-name {
    position: absolute; left: 0; right: 0; top: 222px;
    text-align: center;
    font-size: 40px; font-weight: 700; letter-spacing: -0.2px;
    color: var(--ink);
  }
  .row-bottom .brand-name { top: 220px; }

  /* Back */
  .accent-panel { position: absolute; inset: 0; width: 100%; height: 100%; }
  .accent-panel--sky  { fill: var(--sky); }
  .accent-panel--leaf { fill: var(--leaf); }

  .contact-list {
    position: absolute; right: 48px; top: 46px;
    text-align: right; list-style: none;
    font-size: 16px; line-height: 21px;
    color: var(--ink-dark);
  }
  .contact-rule {
    position: absolute; left: 478px; top: 28px;
    width: 2px; height: 202px;
  }
  .contact-rule--sky  { background: var(--sky); }
  .contact-rule--leaf { background: var(--leaf); }

  .person {
    position: absolute; left: 14px; top: 120px;
    color: var(--white);
    font-size: 17px; line-height: 23px;
  }
  .person-name { font-weight: 700; }
  .person-title { font-weight: 400; }

  .site {
    position: absolute; left: 26px; top: 240px;
    font-size: 19px; font-weight: 700;
    color: var(--white);
  }
</style>
</head>
<body>
<main class="sheet">

  <section class="card card--front row-top" aria-label="Card front, grey">
    <span class="brand-dot brand-dot--sky"></span>
    <p class="brand-name">Outreach2Kindness</p>
  </section>

  <section class="card card--back row-top" aria-label="Card back, blue">
    <svg class="accent-panel accent-panel--sky" viewBox="0 0 519 279" preserveAspectRatio="none" aria-hidden="true">
      <polygon points="0,0 131,0 259,279 0,279"/>
    </svg>
    <ul class="contact-list">
      <li>outreach2kindness@mailbrook.com</li>
      <li>callowaym1@brinmoreu.edu</li>
    </ul>
    <span class="contact-rule contact-rule--sky"></span>
    <div class="person">
      <p class="person-name">Morwenna Calloway</p>
      <p class="person-title">Marketing Consultant</p>
    </div>
    <p class="site">Outreach2Kindness.com</p>
  </section>

  <section class="card card--front row-bottom" aria-label="Card front, white">
    <span class="brand-dot brand-dot--leaf"></span>
    <p class="brand-name">Outreach2Kindness</p>
  </section>

  <section class="card card--back row-bottom" aria-label="Card back, green">
    <svg class="accent-panel accent-panel--leaf" viewBox="0 0 519 279" preserveAspectRatio="none" aria-hidden="true">
      <polygon points="0,0 131,0 259,279 0,279"/>
    </svg>
    <ul class="contact-list">
      <li>outreach2kindness@mailbrook.com</li>
      <li>callowaym1@brinmoreu.edu</li>
    </ul>
    <span class="contact-rule contact-rule--leaf"></span>
    <div class="person">
      <p class="person-name">Morwenna Calloway</p>
      <p class="person-title">Marketing Consultant</p>
    </div>
    <p class="site">Outreach2Kindness.com</p>
  </section>

</main>
</body>
</html>
```